BirchLane Hotel
BUSINESS CARDS, LETTERHEAD, ENVELOPES, FAX COVER, EMAIL SIGNATURE, signage, car
BirchLane Hotel - Hospitality Industry
Creative Brief
Simple
DOHYUN KWAK
President & C.E.O
B2 Sora Bldg. 412-5 Mokhwa-dong, Seocho-gu, Seoul, 137-914, Korea
oliver@blhotelgroup.com
www.blhotelgroup.com
BirchLane Pohang: 218-4 Hwajin-dong, Bukgu, Pohang, Korea BirchLane Gunsan: 457 Maeryeong-dong, Gunsan, Korea

```html
<!DOCTYPE html>
<html lang="en">
<head>
<meta charset="utf-8">
<title>BirchLane Hotel — Business Card</title>
<link rel="stylesheet" href="https://fonts.googleapis.com/css2?family=Arimo:wght@400;700&display=swap">
<style>
  :root {
    --backdrop: #7f8681;
    --card: #ffffff;
    --leaf: #8dc63f;
    --ink: #2b2b2b;
    --text: #4a4a4a;
  }
  * { box-sizing: border-box; margin: 0; padding: 0; }
  html, body {
    width: 1200px; height: 847px; overflow: hidden;
    background: var(--backdrop);
    font-family: "Arimo", Arial, sans-serif;
  }
  .stage { position: relative; width: 1200px; height: 847px; }
  .card {
    position: absolute;
    width: 540px; height: 310px;
    background: var(--card);
    box-shadow: 0 6px 14px rgba(0,0,0,.25);
  }
  .card::before, .card::after {
    content: ""; position: absolute; top: 0; bottom: 0; width: 20px; background: var(--leaf);
  }
  .card::before { left: 0; }
  .card::after { right: 0; }
  .card--front { left: 45px; top: 140px; }
  .card--back { left: 615px; top: 400px; }

  .brand { position: absolute; display: flex; align-items: center; gap: 10px; }
  .brand__square { width: 14px; height: 14px; background: var(--leaf); flex: none; }
  .brand__name { font-weight: 700; color: var(--ink); font-size: 24px; letter-spacing: -.3px; white-space: nowrap; }
  .card--front .brand { right: 56px; top: 120px; }
  .card--back .brand { left: 62px; top: 145px; }
  .card--back .brand__name { font-size: 19px; }
  .card--back .brand__square { width: 11px; height: 11px; }

  .person { position: absolute; left: 42px; top: 130px; }
  .person__name { color: var(--leaf); font-weight: 700; font-size: 17px; letter-spacing: .4px; }
  .person__title { color: var(--text); font-size: 9.5px; margin-top: 2px; }
  .contact { position: absolute; left: 42px; top: 190px; color: var(--text); font-size: 9.5px; line-height: 1.45; }
  .contact__address { margin-top: 10px; }

  .branches { position: absolute; left: 300px; top: 170px; font-size: 9.5px; color: var(--text); line-height: 1.35; }
  .branch + .branch { margin-top: 9px; }
  .branch__city { color: var(--leaf); font-weight: 700; font-size: 10.5px; }
</style>
</head>
<body>
<main class="stage">
  <section class="card card--front">
    <div class="brand">
      <span class="brand__square"></span>
      <span class="brand__name">BirchLane Hotel</span>
    </div>
    <div class="person">
      <div class="person__name">DOHYUN KWAK</div>
      <div class="person__title">President &amp; C.E.O</div>
    </div>
    <div class="contact">
      <div>phone: 02-519-3084</div>
      <div>cell: 010-4861-2207</div>
      <div>fax: 02-519-3087</div>
      <div>email: oliver@blhotelgroup.com</div>
      <div class="contact__address">B2 Sora Bldg. 412-5 Mokhwa-dong<br>Seocho-gu, Seoul, 137-914, Korea</div>
    </div>
  </section>

  <section class="card card--back">
    <div class="brand">
      <span class="brand__square"></span>
      <span class="brand__name">BirchLane Hotel</span>
    </div>
    <div class="branches">
      <div class="branch">
        <div class="branch__city">Pohang:</div>
        <div>218-4 Hwajin-dong, Bukgu, Pohang, Korea</div>
      </div>
      <div class="branch">
        <div class="branch__city">Gunsan:</div>
        <div>457 Maeryeong-dong, Gunsan, Korea</div>
      </div>
    </div>
  </section>
</main>
</body>
</html>
```